ashby paving works

Needs to have phone number 0412885107 and email marklowry@pavemail.com.au.
ABN 27613048852
name mark lowry

For all your concreting solutions
Excavation
Exposed & colour concrete
House & shed slabs
Driveways
Landing & steps

Contact Information for Business Card

ph 0412885107
email marklowry@pavemail.com.au.
ABN 27613048852
name mark lowry

```html
<!DOCTYPE html>
<html lang="en">
<head>
<meta charset="utf-8">
<title>Ashby Paving Works – Business Card</title>
<link href="https://fonts.googleapis.com/css2?family=Alegreya+Sans+SC:wght@300;400&family=Alegreya+Sans:wght@400&family=Montserrat:wght@500;600&display=swap" rel="stylesheet">
<style>
  :root{
    --page:#ffffff;
    --orange:#e8621f;
    --orange-dark:#c9501a;
    --orange-light:#ef7a35;
    --charcoal:#363636;
    --charcoal-soft:#5a5a5a;
    --grey-text:#666666;
    --white:#ffffff;
  }
  html,body{margin:0;padding:0;width:978px;height:1200px;overflow:hidden;background:var(--page);}
  .canvas{position:relative;width:978px;height:1200px;}
  .card{position:absolute;left:136px;width:704px;height:402px;overflow:hidden;box-shadow:0 10px 30px rgba(0,0,0,.18);}
  .card--front{top:186px;}
  .card--back{top:608px;}
  .card__bg{position:absolute;inset:0;width:100%;height:100%;}
  .texture-area{position:absolute;left:0;top:0;width:704px;height:402px;}

  .brand-mark{position:absolute;left:62px;top:112px;width:58px;height:58px;background:var(--orange);}
  .brand-rule{position:absolute;left:154px;top:90px;width:2px;height:104px;background:var(--orange);}
  .brand{position:absolute;left:163px;top:114px;width:266px;text-align:center;font-family:"Montserrat",sans-serif;}
  .brand__name{color:var(--orange);font-weight:600;font-size:21px;letter-spacing:-.2px;line-height:22px;}
  .brand__sub{display:flex;align-items:center;gap:10px;color:var(--grey-text);font-weight:500;font-size:15px;letter-spacing:3px;line-height:18px;}
  .brand__sub::before,.brand__sub::after{content:"";flex:1;height:1.5px;background:var(--grey-text);}
  .brand__phone{color:var(--orange);font-weight:500;font-size:15px;letter-spacing:2.5px;line-height:18px;}

  .person-icon{position:absolute;border:2px solid var(--orange);}
  .person-icon--front{left:198px;top:252px;width:26px;height:26px;}
  .person-icon--back{left:262px;top:34px;width:16px;height:16px;}
  .person{position:absolute;font-family:"Alegreya Sans SC",sans-serif;font-weight:300;white-space:nowrap;}
  .person--front{left:250px;top:244px;font-size:46px;color:var(--grey-text);line-height:54px;}
  .person--back{left:288px;top:32px;font-size:26px;color:var(--white);line-height:30px;}

  .contact{position:absolute;height:53px;}
  .contact svg{position:absolute;inset:0;}
  .contact__text{position:absolute;top:0;height:53px;display:flex;align-items:center;color:var(--charcoal);white-space:nowrap;}
  .contact--phone{left:225px;top:88px;width:282px;}
  .contact--email{left:118px;top:189px;width:497px;}
  .contact--abn{left:220px;top:290px;width:293px;}
  .num{font-family:"Alegreya Sans",sans-serif;font-size:23px;letter-spacing:.5px;}
  .mail{font-family:"Montserrat",sans-serif;font-weight:500;font-size:16px;letter-spacing:.6px;}
  .abn-label{font-family:"Montserrat",sans-serif;font-weight:600;font-size:12px;fill:var(--orange);}

  .mini-brand{position:absolute;left:46px;top:261px;width:35px;height:35px;background:var(--orange);}
  .mini-text{position:absolute;left:98px;top:278px;transform-origin:0 0;transform:rotate(45deg);font-family:"Montserrat",sans-serif;line-height:11px;}
  .mini-text__name{color:var(--orange);font-weight:600;font-size:10px;}
  .mini-text__sub{color:var(--grey-text);font-size:8px;letter-spacing:1.5px;font-weight:500;}
  .mini-text__phone{color:var(--orange);font-size:8px;letter-spacing:1px;font-weight:500;}
</style>
</head>
<body>
<main class="canvas">

  <section class="card card--front" aria-label="Business card front">
    <svg class="card__bg" viewBox="0 0 704 402" preserveAspectRatio="none" aria-hidden="true">
      <defs>
        <linearGradient id="front-silver" x1="0" y1="0" x2="1" y2="1">
          <stop offset="0" stop-color="#e9e9e9"/><stop offset="1" stop-color="#c9c9c9"/>
        </linearGradient>
      </defs>
      <rect width="704" height="402" fill="url(#front-silver)"/>
      <polygon points="435,0 704,0 704,370 387,52" fill="var(--charcoal)"/>
      <polygon points="470,0 640,0 704,64 704,250 560,106" fill="var(--charcoal-soft)" opacity=".55"/>
      <polygon points="335,0 435,0 387,52" fill="var(--orange)"/>
      <polygon points="0,140 263,402 0,402" fill="var(--charcoal)"/>
    </svg>
    <svg class="texture-area" viewBox="0 0 704 402" role="img" aria-label="Faceted orange geometric texture in the lower left corner">
      <defs>
        <linearGradient id="texture-fill" x1="0" y1="0" x2="1" y2="1">
          <stop offset="0" stop-color="var(--orange-dark)"/><stop offset="1" stop-color="var(--orange-light)"/>
        </linearGradient>
      </defs>
      <polygon points="0,218 52,270 95,230 150,285 98,337 163,402 0,402" fill="url(#texture-fill)"/>
    </svg>
    <div class="brand-mark" aria-hidden="true"></div>
    <div class="brand-rule" aria-hidden="true"></div>
    <div class="brand">
      <div class="brand__name">ASHBY PAVING</div>
      <div class="brand__sub">WORKS</div>
      <div class="brand__phone">0412885107</div>
    </div>
    <div class="person-icon person-icon--front" aria-hidden="true"></div>
    <div class="person person--front">Mark Lowry</div>
  </section>

  <section class="card card--back" aria-label="Business card back">
    <svg class="card__bg" viewBox="0 0 704 402" preserveAspectRatio="none" aria-hidden="true">
      <defs>
        <radialGradient id="back-dark" cx=".55" cy=".45" r=".7">
          <stop offset="0" stop-color="#4a4a4a"/><stop offset="1" stop-color="#2f2f2f"/>
        </radialGradient>
        <linearGradient id="back-light" x1="0" y1="0" x2="1" y2="1">
          <stop offset="0" stop-color="#f4f4f4"/><stop offset="1" stop-color="#d6d6d6"/>
        </linearGradient>
      </defs>
      <rect width="704" height="402" fill="url(#back-dark)"/>
      <polygon points="0,0 184,0 0,184" fill="var(--charcoal-soft)" opacity=".85"/>
      <polygon points="184,0 260,0 30,230 0,200 0,184" fill="#2c2c2c" opacity=".6"/>
      <polygon points="0,160 247,402 0,402" fill="url(#back-light)"/>
    </svg>

    <div class="person-icon person-icon--back" aria-hidden="true"></div>
    <div class="person person--back">Mark Lowry</div>

    <div class="contact contact--phone">
      <svg viewBox="0 0 282 53" width="282" height="53" aria-hidden="true">
        <defs><linearGradient id="tip1" x1="0" y1="0" x2="1" y2="1"><stop offset="0" stop-color="#fff"/><stop offset="1" stop-color="#9a9a9a"/></linearGradient></defs>
        <polygon points="26,0 256,0 282,26.5 256,53 26,53 0,26.5" fill="var(--orange)"/>
        <polygon points="212,0 256,0 282,26.5 256,53 248,53" fill="url(#tip1)"/>
        <polygon points="26,2 50,26.5 26,51 2,26.5" fill="var(--charcoal)" stroke="var(--orange)" stroke-width="2"/>
        <path d="M20 17 q-3 3 0 9 q4 7 9 9 q4 1 5 -2 l-4 -3 l-2 2 q-4 -2 -5 -6 l2 -2 z" fill="none" stroke="var(--orange)" stroke-width="1.6"/>
      </svg>
      <span class="contact__text num" style="left:78px">0412885107</span>
    </div>

    <div class="contact contact--email">
      <svg viewBox="0 0 497 53" width="497" height="53" aria-hidden="true">
        <defs><linearGradient id="tip2" x1="0" y1="0" x2="1" y2="1"><stop offset="0" stop-color="#fff"/><stop offset="1" stop-color="#9a9a9a"/></linearGradient></defs>
        <polygon points="26,0 471,0 497,26.5 471,53 26,53 0,26.5" fill="var(--orange)"/>
        <polygon points="427,0 471,0 497,26.5 471,53 463,53" fill="url(#tip2)"/>
        <polygon points="26,2 50,26.5 26,51 2,26.5" fill="var(--charcoal)" stroke="var(--orange)" stroke-width="2"/>
        <rect x="15" y="20" width="23" height="14" fill="var(--orange)"/>
        <path d="M15 20 l11.5 8 l11.5 -8" fill="none" stroke="var(--charcoal)" stroke-width="1.4"/>
      </svg>
      <span class="contact__text mail" style="left:82px">MARKLOWRY@PAVEMAIL.COM.AU.</span>
    </div>

    <div class="contact contact--abn">
      <svg viewBox="0 0 293 53" width="293" height="53" aria-hidden="true">
        <defs><linearGradient id="tip3" x1="0" y1="0" x2="1" y2="1"><stop offset="0" stop-color="#fff"/><stop offset="1" stop-color="#9a9a9a"/></linearGradient></defs>
        <polygon points="26,0 267,0 293,26.5 267,53 26,53 0,26.5" fill="var(--orange)"/>
        <polygon points="223,0 267,0 293,26.5 267,53 259,53" fill="url(#tip3)"/>
        <polygon points="26,2 50,26.5 26,51 2,26.5" fill="var(--charcoal)" stroke="var(--orange)" stroke-width="2"/>
        <text x="26" y="31" text-anchor="middle" class="abn-label">ABN</text>
      </svg>
      <span class="contact__text num" style="left:85px">27613048852</span>
    </div>

    <div class="mini-brand" aria-hidden="true"></div>
    <div class="mini-text">
      <div class="mini-text__name">ASHBY PAVING</div>
      <div class="mini-text__sub">WORKS</div>
      <div class="mini-text__phone">0412885107</div>
    </div>
  </section>

</main>
</body>
</html>
```